Business Card Design Project

Mabel's Tonics is a natural skincare business and we need a business card designed. The company focuses on natural products and will be launching with body scrubs and bath fizzies and our mission statement is: To deliver high quality natural beauty products at a good value. It's two cards - one design - the only information changing would be name and email address

Target Market(s)

Females ages 20-50

Industry/Entity Type

Business

Requirements
Must have
• Mabel's Tonics

Corinne Halvorsen-Pitt
T: 800-417-9368
E: Corinne@MabelsTonics.example
W: www.MabelsTonics.example

Ulrich Benedetti
T: 800-417-9368
E: Ulrich@MabelsTonics.example
W: www.MabelsTonics.example
Nice to have
• I'd like to use the colors or text found at www.mabelstonics.example but I'm open to suggestions since design isn't set in stone yet. I would also like to have the words .....a little bit of magic somewhere under the company name in a different type of font. I would like a design that feels clean and maybe a retro feel to it - front and back would be nice but not mandatory

```html
<!DOCTYPE html>
<html lang="en">
<head>
<meta charset="utf-8">
<title>Mabel's Tonics – Business Card</title>
<link rel="stylesheet" href="https://fonts.googleapis.com/css2?family=Gelasio:ital,wght@0,400;1,400;1,700&display=swap">
<style>
  :root {
    --page: #ffffff;
    --violet-main: #6340dd;
    --violet-edge: #8a4fe6;
    --aqua-edge: #7fd3e6;
    --logo-panel: #ffffff;
    --brand-ink: #6a2bc8;
    --name-ink: #9ff0f0;
    --detail-ink: #ffffff;
  }
  html, body {
    margin: 0;
    padding: 0;
    overflow: hidden;
    background: var(--page);
  }
  .canvas {
    position: relative;
    width: 1200px;
    height: 763px;
    overflow: hidden;
    background: var(--page);
    font-family: "Gelasio", Georgia, serif;
  }
  .card-shape {
    position: absolute;
    left: 0;
    top: 0;
  }
  .logo-panel {
    position: absolute;
    left: 448px;
    top: 210px;
    width: 458px;
    height: 123px;
    background: var(--logo-panel);
    border-radius: 16px;
    display: flex;
    align-items: center;
    justify-content: center;
  }
  .brand-name {
    margin: 0;
    font-size: 54px;
    font-weight: 400;
    line-height: 1;
    color: var(--brand-ink);
    white-space: nowrap;
  }
  .contact {
    position: absolute;
    left: 140px;
    top: 468px;
    margin: 0;
    color: var(--detail-ink);
  }
  .contact-name {
    position: relative;
    margin: 0 0 2px;
    font-size: 26px;
    font-style: italic;
    font-weight: 700;
    color: var(--name-ink);
    white-space: nowrap;
  }
  .star {
    position: absolute;
    color: var(--detail-ink);
    font-size: 16px;
    font-style: normal;
    top: 8px;
  }
  .star-left { left: -24px; }
  .star-right { left: 316px; }
  .contact-line {
    margin: 0;
    font-size: 23px;
    line-height: 30px;
    white-space: nowrap;
  }
</style>
</head>
<body>
<main class="canvas">
  <svg class="card-shape" width="1200" height="763" viewBox="0 0 1200 763" aria-hidden="true">
    <defs>
      <clipPath id="card-area">
        <rect x="61" y="147" width="897" height="499"/>
      </clipPath>
    </defs>
    <g clip-path="url(#card-area)">
      <ellipse cx="538" cy="425" rx="545" ry="266" transform="rotate(-22 538 425)" fill="var(--aqua-edge)"/>
      <ellipse cx="486" cy="425" rx="525" ry="266" transform="rotate(-22 486 425)" fill="var(--violet-edge)"/>
      <ellipse cx="516" cy="425" rx="525" ry="260" transform="rotate(-22 516 425)" fill="var(--violet-main)"/>
    </g>
  </svg>

  <div class="logo-panel">
    <p class="brand-name">Mabel's Tonics</p>
  </div>

  <section class="contact">
    <p class="contact-name"><span class="star star-left">★</span>Ulrich Benedetti<span class="star star-right">★</span></p>
    <p class="contact-line">T: 800-417-9368</p>
    <p class="contact-line">E: ulrich@mabelstonics.example</p>
    <p class="contact-line">W: www.mabelstonics.example</p>
  </section>
</main>
</body>
</html>
```